Business Card Design for Mortgage Broking Business

We need to redesign the business card. Mortgage broking business, doing home loan and commercial loans, existing logo, also QLPN member logo. design style needs to be simple, professional, elegant.

once final, need to setup for a team of different names and contact details.

Industry/Entity Type

Loan

Contact Information for Business Card

Name; Mobile; Email; Address; Tel; Fax; Australian Credit Licence: 782316

```html
<!DOCTYPE html>
<html lang="en">
<head>
<meta charset="utf-8">
<title>Harbourline Lending – Business Card</title>
<link rel="stylesheet" href="https://fonts.googleapis.com/css2?family=Lato:wght@400;700;900&display=swap">
<style>
  :root {
    --bg: #242426;
    --brand-green: #3bb54a;
    --brand-blue: #2e3a96;
    --accent-sky: #29a3dd;
    --paper: #ffffff;
    --ink: #1d1d1f;
    --ink-soft: #3a3a3c;
  }
  * { box-sizing: border-box; margin: 0; padding: 0; }
  html, body { width: 1200px; height: 800px; overflow: hidden; }
  body {
    background: var(--bg);
    font-family: "Lato", Arial, sans-serif;
    position: relative;
  }
  .card {
    position: absolute;
    top: 250px;
    width: 520px;
    height: 300px;
    border-radius: 22px;
    overflow: hidden;
  }
  .card--front { left: 50px; background: var(--brand-green); }
  .card--back { left: 630px; background: var(--paper); color: var(--ink); }

  /* Front */
  .front-wordmark {
    position: absolute;
    left: 0; right: 0; top: 100px;
    text-align: center;
    color: var(--paper);
    font-weight: 900;
    font-size: 40px;
    letter-spacing: 0.5px;
    display: flex; align-items: center; justify-content: center; gap: 14px;
  }
  .front-wordmark .mark-square {
    width: 34px; height: 34px; background: var(--paper); display: inline-block;
  }
  .member-badge {
    position: absolute;
    left: 300px; top: 200px;
    width: 96px; height: 34px;
    border: 2px solid #1c1c1c;
  }

  /* Back */
  .side-tab {
    position: absolute;
    left: -14px; top: 108px;
    width: 28px; height: 28px;
    border-radius: 50%;
    background: var(--accent-sky);
  }
  .contact { position: absolute; left: 54px; top: 104px; }
  .contact__name { color: var(--brand-green); font-weight: 700; font-size: 16px; }
  .contact__role { font-size: 13px; color: var(--ink-soft); margin-top: 1px; }
  .contact__address { font-size: 13px; color: var(--ink-soft); margin-top: 30px; line-height: 1.3; }
  .contact__lines { list-style: none; margin-top: 22px; font-size: 13.5px; color: var(--ink-soft); }
  .contact__lines li { display: flex; align-items: center; gap: 7px; line-height: 1.25; }
  .contact__lines svg { width: 11px; height: 11px; fill: var(--brand-green); flex: none; }

  .brand { position: absolute; right: 40px; top: 150px; text-align: center; }
  .brand__name {
    display: flex; align-items: center; gap: 8px;
    color: var(--brand-blue); font-weight: 900; font-size: 22px;
  }
  .brand__name .mark-square { width: 22px; height: 22px; background: var(--brand-blue); }
  .brand__tagline { color: var(--brand-blue); font-weight: 700; font-size: 12px; margin-top: 4px; letter-spacing: 0.5px; }
  .brand__licence { color: var(--ink); font-weight: 700; font-size: 12.5px; margin-top: 3px; }
</style>
</head>
<body>
  <section class="card card--front" aria-label="Card front">
    <div class="front-wordmark"><span class="mark-square"></span>Harbourline Lending</div>
    <div class="member-badge" role="img" aria-label="QLPN approved credit adviser badge"></div>
  </section>

  <section class="card card--back" aria-label="Card back">
    <span class="side-tab"></span>
    <div class="contact">
      <p class="contact__name">Marcus Hale</p>
      <p class="contact__role">Director</p>
      <p class="contact__address">Address Line One<br>Address line 2</p>
      <ul class="contact__lines">
        <li><svg viewBox="0 0 12 12"><path d="M1 3c0-1 1-2 2-2h1l1 3-1 1c1 2 2 3 4 4l1-1 3 1v1c0 1-1 2-2 2C5 12 0 7 1 3z"/></svg>000-111-2345</li>
        <li><svg viewBox="0 0 12 12"><path d="M3 0h6a1 1 0 0 1 1 1v10a1 1 0 0 1-1 1H3a1 1 0 0 1-1-1V1a1 1 0 0 1 1-1zm0 2v7h6V2z"/></svg>999-888-7776</li>
        <li><svg viewBox="0 0 12 12"><path d="M3 0h6v3H3zM1 4h10a1 1 0 0 1 1 1v4H9v3H3V9H0V5a1 1 0 0 1 1-1zm3 5v2h4V9z"/></svg>012-345-6789</li>
        <li><svg viewBox="0 0 12 12"><path d="M0 2h12v8H0zm1 1v1l5 3 5-3V3L6 6z"/></svg>info@yourmail.com</li>
      </ul>
    </div>
    <div class="brand">
      <div class="brand__name"><span class="mark-square"></span>Harbourline Lending</div>
      <p class="brand__tagline">Mortgage Planners</p>
      <p class="brand__licence">Credit Licence: 782316</p>
    </div>
  </section>
</body>
</html>
```